Newspaper Ad for a new concept medical clinic

I have uploaded a sample ad. I would prefer the black areas to be the same color blue as the word CareVane in the attached file. Instead of a doctor I would like a concerned or worried looking middle age couple 40s/50s as a picture.

702 number will need to change to a toll free number that I will have available next week.
Change web address to www.brivamd.example

I would like the bullet points to be changed as follows:
- Affordable Access To Board Certified Physician
- Committment To Excellence In Primary Medical Care
- $10 Office Visits / No Charge Telemedicine Visits
- Adults - $69/month & Teens to Age 26 - $19/month
- Lowest Rates For Lab Tests, Imaging, and Medications

Keep the As Seen In section unchanged
Updates

Ii would like full color. Also I will call the local newspaper today and find the exact dimensenions and update everyone. Thank you all for interest and input.

3 columns(4.9" wide) by 5.25" tall

Please review your submission for readability at the size proposed. The actual ad size is 4.9" wide by 5.25 in tall. There are many wonderful submissions. I am truly impressed.

Full Color

Make sure the copy is readable at this ad size. My last request is for you to add the following term somewhere: Limited Enrollment Call Now

Industry/Entity Type

Medical

```html
<!DOCTYPE html>
<html lang="en">
<head>
<meta charset="utf-8">
<title>CareVane Direct Primary Care – Newspaper Ad</title>
<link rel="stylesheet" href="https://fonts.googleapis.com/css2?family=Fjalla+One&family=Arimo:wght@400;700&family=Open+Sans:wght@500;600;700&display=swap">
<style>
  :root {
    --brand-blue: #1f74b9;
    --accent-orange: #f39a1e;
    --white: #ffffff;
    --ink: #111111;
    --rule: #c9dcef;
    --fine-print: #d7e6f4;
    --page: #ffffff;
    --photo-light: #e9e9e9;
    --photo-mid: #bdbdbd;
    --photo-dark: #7d7d7d;
  }
  * { margin: 0; padding: 0; box-sizing: border-box; }
  html, body { width: 935px; height: 1200px; overflow: hidden; background: var(--page); }
  /* 4.9in x 5.25in ad proportion */
  .ad {
    position: absolute;
    left: 0; top: 99px;
    width: 935px;
    height: 1002px;
    background: var(--brand-blue);
    overflow: hidden;
    font-family: "Arimo", Arial, sans-serif;
  }
  .headline {
    position: absolute;
    top: 0; left: 0; width: 100%; height: 128px;
    display: flex; align-items: center; justify-content: center;
    font-family: "Fjalla One", "Arial Narrow", sans-serif;
    font-weight: 400;
    font-size: 72px;
    color: var(--white);
    letter-spacing: 0.5px;
  }
  .hero-photo {
    position: absolute;
    top: 128px; left: 4px;
    width: 927px; height: 278px;
    background: linear-gradient(100deg, var(--photo-mid) 0%, var(--photo-light) 38%, var(--photo-light) 62%, var(--photo-dark) 100%);
  }
  .hero-cta {
    position: absolute;
    left: 520px; top: 244px;
    font-size: 46px; font-weight: 700; color: var(--ink);
    line-height: 1;
  }
  .hero-web {
    position: absolute;
    left: 510px; top: 334px;
    font-size: 34px; font-weight: 700; color: var(--ink);
    line-height: 1;
  }
  .benefits {
    position: absolute;
    left: 43px; top: 420px;
    list-style: none;
    color: var(--white);
    font-size: 26px; font-weight: 700;
    line-height: 44px;
  }
  .enrollment {
    position: absolute;
    left: 0; top: 652px; width: 100%;
    text-align: center;
    font-family: "Open Sans", Arial, sans-serif;
    font-weight: 700;
    font-size: 30px;
    line-height: 40px;
    letter-spacing: 1.5px;
    text-transform: uppercase;
    color: var(--white);
    background: var(--accent-orange);
  }
  .press {
    position: absolute;
    left: 59px; top: 706px; width: 821px;
  }
  .press-label {
    display: flex; align-items: center; gap: 14px;
    color: var(--white); font-size: 15px; letter-spacing: 1px;
    line-height: 18px;
  }
  .press-label::before, .press-label::after {
    content: ""; flex: 1; height: 1px; background: var(--rule);
  }
  .press-badges { position: relative; height: 76px; }
  .press-badge {
    position: absolute;
    height: 26px;
    background: rgba(255,255,255,0.85);
    border-radius: 3px;
  }
  .press-rule { height: 1px; background: var(--rule); margin-top: 4px; }
  .disclaimer {
    position: absolute;
    top: 814px; left: 0; width: 100%;
    text-align: center;
    color: var(--fine-print);
    font-size: 19px;
    line-height: 24px;
  }
  .brand-panel {
    position: absolute;
    top: 852px; left: 0; width: 100%; height: 150px;
    background: var(--white);
  }
  .brand-name {
    position: absolute;
    left: 232px; top: 0;
    font-family: "Open Sans", Arial, sans-serif;
    font-weight: 500;
    font-size: 76px;
    line-height: 100px;
    color: var(--brand-blue);
    letter-spacing: -0.5px;
  }
  .brand-dot {
    position: absolute;
    left: 598px; top: 26px;
    width: 48px; height: 48px;
    border-radius: 50%;
    background: var(--accent-orange);
  }
  .brand-tagline {
    position: absolute;
    left: 235px; top: 98px;
    font-family: "Open Sans", Arial, sans-serif;
    font-weight: 600;
    font-size: 34px;
    line-height: 44px;
    color: var(--accent-orange);
  }
</style>
</head>
<body>
  <main class="ad">
    <h1 class="headline">Can’t Afford Health Benefits?</h1>

    <div class="hero-photo" role="img" aria-label="Photo of a worried middle-aged couple sitting apart, heads in hands"></div>
    <p class="hero-cta">Call to sign up</p>
    <p class="hero-web">www.brivamd.example</p>

    <ul class="benefits">
      <li>- Affordable Access To Board Certified Physician</li>
      <li>- Committment To Excellence In Primary Medical Care</li>
      <li>- $10 Office Visits / No Charge Telemedicine Visits</li>
      <li>- Adults - $69/month &amp; Teens to Age 26 - $19/month</li>
      <li>- Lowest Rates For Lab Tests, Imaging, and Medications</li>
    </ul>

    <p class="enrollment">Limited Enrollment – Call Now</p>

    <section class="press" aria-label="As seen in">
      <p class="press-label">AS SEEN IN</p>
      <div class="press-badges">
        <span class="press-badge" style="left:0; top:10px; width:283px;"></span>
        <span class="press-badge" style="left:354px; top:10px; width:112px;"></span>
        <span class="press-badge" style="left:548px; top:10px; width:273px;"></span>
        <span class="press-badge" style="left:268px; top:44px; width:280px;"></span>
      </div>
      <div class="press-rule"></div>
    </section>

    <p class="disclaimer">This is not an offer of insurance. Please call for details.</p>

    <footer class="brand-panel">
      <span class="brand-name">CareVane</span>
      <span class="brand-dot" aria-hidden="true"></span>
      <span class="brand-tagline">Direct Primary Care</span>
    </footer>
  </main>
</body>
</html>
```